bramblewood mental health web page

this is to be a single page with no links - will function just like an add.
will have 2 biographies
contact info.
Updates

Dear Designers - most of these are too complex.

 Just want one page with contact details (yet to be sorted). No email contact as we can't monitor all emails and if person emails saying suicidal I am potentially accountable if they are successful. Hence- this is just like a listing in a phone book. 
2 photos - one of me the other my husband - with a little blurb next to our names.
No info on fees or appointments etc
I am legally not allowed use language like - "what sets us apart" - it suggests we are better than other clinicians and that is illegal. 
NO EMOTIVE PHOTOS PLEASE! 

Target Market(s)

clients wanting check background and contact information.

Industry/Entity Type

Mental Health

Requirements
Must have
• NEW LOGO
space for photographs
Old web page to complicated
http://wbtk.net.au/index.shtml
Should not have
• anything that flashes.

```html
<!DOCTYPE html>
<html lang="en">
<head>
<meta charset="utf-8">
<title>Bramblewood Mental Health – Curriculum Vitae</title>
<link href="https://fonts.googleapis.com/css2?family=Arimo:wght@400;700&family=Archivo+Narrow:wght@700&family=Great+Vibes&family=Open+Sans:ital,wght@0,400;0,600;0,700;1,400&display=swap" rel="stylesheet">
<style>
:root{
  --ink:#111111;
  --brand:#2b3b4e;
  --paper:#ffffff;
  --col-grey:#878787;
  --col-blue:#2f4b62;
  --photo:#000000;
}
*{margin:0;padding:0;box-sizing:border-box}
html,body{width:800px;height:1200px;overflow:hidden;background:var(--paper)}
.page{position:relative;width:800px;height:1200px;color:var(--ink);font-family:"Arimo",Arial,sans-serif}
.brand{position:absolute;left:16px;top:15px;height:76px;display:flex;align-items:center;gap:16px}
.brand-mark{width:60px;height:60px;background:var(--brand)}
.brand-name{font-family:"Arimo",Arial,sans-serif;font-weight:400;font-size:23px;line-height:27px;color:var(--brand);letter-spacing:1px;text-transform:uppercase;white-space:nowrap}
.brand-name span{display:block}
.company-ids{position:absolute;left:24px;top:98px;font-size:14px;line-height:17px}
.company-ids b{font-weight:700}
.address{position:absolute;left:410px;top:29px;font-size:15px;font-style:italic;letter-spacing:3.2px;white-space:nowrap}
.phone{position:absolute;left:447px;top:63px;font-size:14px;font-weight:700;white-space:nowrap}
.doc-title{position:absolute;left:0;top:195px;width:800px;text-align:center;font-family:"Archivo Narrow","Arial Narrow",sans-serif;font-weight:700;font-size:19px}
.society{position:absolute;left:0;top:240px;width:800px;text-align:center;font-family:"Great Vibes",cursive;font-size:22px;letter-spacing:6.4px;white-space:nowrap}
.photo{position:absolute;top:280px;width:60px;height:94px;background:var(--photo)}
.photo-left{left:15px}
.photo-right{left:721px}
.clinician{position:absolute;top:295px;font-family:"Open Sans",Verdana,sans-serif;font-size:13px;line-height:18px;letter-spacing:.9px;white-space:nowrap}
.clinician-left{right:422px;text-align:right}
.clinician-right{left:421px}
.clinician .name{font-weight:700}
.clinician .quals{font-style:italic}
.clinician b{font-weight:700}
.cv-column{position:absolute;top:380px;width:390px;height:780px;padding:12px 3px 0 3px;font-size:12.6px;line-height:20.3px}
.cv-left{left:7px;background:var(--col-grey)}
.cv-right{left:401px;background:var(--col-blue)}
.cv-section{margin-bottom:20.3px}
.cv-section h2{font-size:12.6px;font-weight:700;line-height:20.3px}
.cv-section p{text-align:justify}
</style>
</head>
<body>
<main class="page">
  <header>
    <div class="brand">
      <div class="brand-mark"></div>
      <div class="brand-name"><span>Bramblewood</span><span>Mental Health</span></div>
    </div>
    <p class="company-ids"><b>ABN:</b> 41 602 318 947 &nbsp;<b>ACN:</b> 218634097</p>
    <p class="address">24 Fenwick Place, HALLORAN 6031</p>
    <p class="phone">Phone:( 08) 9310 4682 or 0491275836</p>
  </header>

  <h1 class="doc-title">O &amp; M Hollis Family Trust - Curriculum Vitae</h1>
  <p class="society">Members of the Westward Psychological Society</p>

  <div class="photo photo-left" role="img" aria-label="Portrait photo of Maren Hollis"></div>
  <div class="photo photo-right" role="img" aria-label="Portrait photo of Owen Hollis"></div>

  <div class="clinician clinician-left">
    <div class="name">Maren Hollis M. Psych (Clinical)</div>
    <div class="quals">M. Genetic Couns., B.A. (Psych)</div>
    <div>Reg. no: <b>PSY0000481236</b></div>
    <div>Provider no: <b>5830264J</b></div>
  </div>
  <div class="clinician clinician-right">
    <div class="name">Owen Hollis M. Psych (Clinical)</div>
    <div class="quals">M. Genetic Couns., B.A. (Psych)</div>
    <div>Reg. no: <b>PSY##########</b></div>
    <div>Provider no: <b>########</b></div>
  </div>

  <section class="cv-column cv-left">
    <div class="cv-section"><h2>Personal data</h2><p>Place of birth: Sidney<br>Date of birth: 30 April ####<br>Status: Married</p></div>
    <div class="cv-section"><h2>Career Profile</h2><p>Sed ut perspiciatis unde omnis iste natus error sit voluptatem accusantium doloremque laudantium, totam rem aperiam, eaque ipsa quae ab illo inventore veritatis et quasi architecto beatae vitae dicta sunt explicabo. Nemo enim ipsam voluptatem quia voluptas sit aspernatur aut odit aut fugit, sed quia consequuntur magni dolores eos qui ratione voluptatem sequi nesciunt.</p></div>
    <div class="cv-section"><h2>Achievements</h2><p>Lorem ipsum dolor sit amet, consectetur adipisicing elit, sed do eiusmod tempor incididunt ut labore et dolore magna aliqua. Ut enim ad minim veniam, quis nostrud exercitation ullamco laboris nisi ut aliquip ex ea commodo consequat. Duis aute irure dolor in reprehenderit in voluptate velit esse cillum dolore eu fugiat nulla pariatur. Excepteur sint occaecat cupidatat non proident, sunt in culpa qui officia deserunt mollit anim id est laborum.</p></div>
    <div class="cv-section"><h2>Education and Training</h2><p>Lorem ipsum dolor sit amet, consectetur adipisicing elit, sed do eiusmod tempor incididunt ut labore et dolore magna aliqua. Ut enim ad minim veniam, quis nostrud exercitation ullamco laboris nisi ut aliquip ex ea commodo consequat. Duis aute irure dolor in reprehenderit in voluptate velit esse cillum dolore eu fugiat nulla pariatur. Excepteur sint occaecat cupidatat non proident, sunt in culpa qui officia deserunt mollit anim id est laborum.</p></div>
    <div class="cv-section"><h2>Professional Memberships</h2><p>Lorem ipsum dolor sit amet, consectetur adipisicing elit, sed do eiusmod tempor incididunt ut labore et dolore magna aliqua. Ut enim ad minim veniam, quis nostrud exercitation ullamco laboris nisi ut aliquip ex ea commodo consequat.</p></div>
  </section>

  <section class="cv-column cv-right">
    <div class="cv-section"><h2>Personal data</h2><p>Place of birth: Sidney<br>Date of birth: 30 April ####<br>Status: Married</p></div>
    <div class="cv-section"><h2>Career Profile</h2><p>Sed ut perspiciatis unde omnis iste natus error sit voluptatem accusantium doloremque laudantium, totam rem aperiam, eaque ipsa quae ab illo inventore veritatis et quasi architecto beatae vitae dicta sunt explicabo. Nemo enim ipsam voluptatem quia voluptas sit aspernatur aut odit aut fugit, sed quia consequuntur magni dolores eos qui ratione voluptatem sequi nesciunt.</p></div>
    <div class="cv-section"><h2>Achievements</h2><p>Lorem ipsum dolor sit amet, consectetur adipisicing elit, sed do eiusmod tempor incididunt ut labore et dolore magna aliqua. Ut enim ad minim veniam, quis nostrud exercitation ullamco laboris nisi ut aliquip ex ea commodo consequat. Duis aute irure dolor in reprehenderit in voluptate velit esse cillum dolore eu fugiat nulla pariatur. Excepteur sint occaecat cupidatat non proident, sunt in culpa qui officia deserunt mollit anim id est laborum.</p></div>
    <div class="cv-section"><h2>Education and Training</h2><p>Lorem ipsum dolor sit amet, consectetur adipisicing elit, sed do eiusmod tempor incididunt ut labore et dolore magna aliqua. Ut enim ad minim veniam, quis nostrud exercitation ullamco laboris nisi ut aliquip ex ea commodo consequat. Duis aute irure dolor in reprehenderit in voluptate velit esse cillum dolore eu fugiat nulla pariatur. Excepteur sint occaecat cupidatat non proident, sunt in culpa qui officia deserunt mollit anim id est laborum.</p></div>
    <div class="cv-section"><h2>Professional Memberships</h2><p>Lorem ipsum dolor sit amet, consectetur adipisicing elit, sed do eiusmod tempor incididunt ut labore et dolore magna aliqua. Ut enim ad minim veniam, quis nostrud exercitation ullamco laboris nisi ut aliquip ex ea commodo consequat.</p></div>
  </section>
</main>
</body>
</html>
```